Finance Broker helping people meet their personal and business goals

New business card design,
1st look at the old business card so this makes sense.
I DON'T want:
the subtext "For all your Rural and Commercial Finance".
I DON'T want the: "and Management Consultant" words
I DON'T want the old phone: 07 49217305
I DON'T want the fax number: 07 48160923
I DON'T want the email address: tallowcreek@quarnet.com.au
I DON'T want the flower
What I DO want
I DO want the mobile 0418 365 907 (in larger text)
I DO want:
My name: Dennis Harlow-Pike
I DO want: Australian Credit Licence 512964 (Tallow Creek Pty Ltd)
I DO want: Principal Finance Broker
I DO want new email: dennis@plantreasurepath.com.au
I DO want address: PO Box 836, Tarrawin Qld 4871
I DO want the existing logo (PTP on existing card)

Target Market(s)

Business Borrowers, Home Purchasers, and People wanting to finance cars and plant and equipment

Industry/Entity Type

Financial Service

Contact Information for Business Card

See project description

Font styles to use
Serif

Colors

Designer to choose colors to be used in the design.

Requirements
Must have
• See project description
Nice to have
• Black and Yellow colours
Should not have
• See project description

```html
<!DOCTYPE html>
<html lang="en">
<head>
<meta charset="utf-8">
<title>Plan Treasure Path – Business Card</title>
<link rel="stylesheet" href="https://fonts.googleapis.com/css2?family=Kalam:wght@400;700&family=Tinos&display=swap">
<style>
  :root {
    --page: #fefefe;
    --card: #221f20;
    --accent: #fff46d;
    --ink: #ffffff;
  }
  html, body {
    margin: 0;
    width: 1200px;
    height: 1200px;
    overflow: hidden;
    background: var(--page);
  }
  .canvas {
    position: relative;
    width: 1200px;
    height: 1200px;
  }
  .card {
    position: absolute;
    left: 181px;
    top: 367px;
    width: 845px;
    height: 483px;
    background: var(--card);
    color: var(--ink);
    font-family: "Tinos", "Times New Roman", serif;
  }
  .brand {
    position: absolute;
    left: 80px;
    top: 28px;
    width: 458px;
  }
  .brand-name {
    margin: 0;
    font-family: "Tinos", "Times New Roman", serif;
    font-weight: 400;
    font-size: 50px;
    line-height: 1;
    letter-spacing: 1px;
    color: var(--accent);
    text-align: right;
    white-space: nowrap;
  }
  .brand-tagline {
    margin: 4px 0 0;
    font-family: "Kalam", cursive;
    font-size: 25px;
    line-height: 1.1;
    color: var(--ink);
    text-align: right;
    white-space: nowrap;
  }
  .brand-mark {
    position: absolute;
    left: 610px;
    top: 37px;
    width: 72px;
    height: 72px;
    border-radius: 50%;
    background: var(--accent);
  }
  .contact {
    position: absolute;
    left: 0;
    width: 100%;
    text-align: center;
    margin: 0;
    white-space: nowrap;
  }
  .person-name {
    top: 148px;
    font-family: "Kalam", cursive;
    font-weight: 700;
    font-size: 44px;
    letter-spacing: 2px;
    line-height: 1;
  }
  .credentials {
    top: 206px;
    font-size: 25px;
    line-height: 27px;
  }
  .mobile {
    top: 293px;
    font-size: 56px;
    line-height: 1;
  }
  .email {
    top: 388px;
    font-size: 27px;
    line-height: 1;
  }
  .address {
    top: 426px;
    font-size: 27px;
    line-height: 1;
  }
</style>
</head>
<body>
  <main class="canvas">
    <section class="card">
      <div class="brand">
        <p class="brand-name">Plan Treasure Path</p>
        <p class="brand-tagline">A Member of the Tallow Creek Group</p>
      </div>
      <span class="brand-mark" aria-hidden="true"></span>

      <p class="contact person-name">Dennis Harlow-Pike</p>
      <p class="contact credentials">Australian Credit Licence 512964<br>Principal Finance Broker</p>
      <p class="contact mobile">0418 365 907</p>
      <p class="contact email">Email: dennis@plantreasurepath.com.au</p>
      <p class="contact address">PO Box 836, Tarrawin Qld 4871</p>
    </section>
  </main>
</body>
</html>
```